Hot-air ballooning company needs a DL-size flyer

Skylark Aerial Tours is a hot-air ballooning company which flies passengers in the King Valley, Victoria, Australia.
We need a 2-sided DL-size flyer which promotes our hot-air balloon flights and packages.
Most of our customers are couples, and we want the flyer design to communicate safety, adventure, and romance.
The flyer should make the best use of our images which we provide, and we've also included a document with the text for the flyer.
Updates

2 days is not long enough to gather designs, the brief never asked me what my deadline should be.

Target Market(s)

Couples, buyers are majority female, between the ages of 20-60

Industry/Entity Type

Tourism

Font styles to use
Sans Serif

Colors

Designer to choose colors to be used in the design.

Requirements
Must have
• Communicate safety, adventure, and romance
• Use images
Nice to have
• There is a lot of text, it would be great if you could make it look like as little text as possible
Should not have
• No childish designs

```html
<!DOCTYPE html>
<html lang="en">
<head>
<meta charset="utf-8">
<title>Skylark Aerial Tours – DL Flyer</title>
<link rel="stylesheet" href="https://fonts.googleapis.com/css2?family=Dosis:wght@500;600&family=Dancing+Script:wght@500&family=Open+Sans:ital,wght@0,400;0,600;1,400&family=Arimo:wght@700&family=Comfortaa:wght@500&family=Caveat:wght@500&display=swap">
<style>
  :root{
    --page:#e8ecf0;
    --sky-top:#4b88c3;
    --sky-mid:#7fa9cf;
    --mist:#a9b9c6;
    --land:#6f7a5c;
    --orange:#ee5a24;
    --orange-light:#f7903a;
    --orange-dome:#f27a2e;
    --white:#ffffff;
    --back-blue:#5a8fcc;
    --back-blue-low:#8fb3dc;
    --paper:#fbfbfb;
  }
  *{box-sizing:border-box;margin:0;padding:0}
  html,body{width:1200px;height:848px;overflow:hidden;background:var(--page)}
  .canvas{position:relative;width:1200px;height:848px}
  .card{position:absolute;width:720px;height:362px;border:4px solid var(--white);overflow:hidden;box-shadow:0 10px 24px rgba(40,60,90,.18)}
  .card--front{left:40px;top:40px}
  .card--back{left:440px;top:448px}
  .abs{position:absolute}
  .center{text-align:center;width:100%;left:0}

  /* front */
  .hero-photo{left:0;top:0;width:100%;height:302px;background:linear-gradient(180deg,var(--sky-top) 0%,var(--sky-mid) 55%,var(--mist) 78%,var(--land) 100%)}
  .front-copy{left:256px;width:446px;color:var(--white);text-align:center;white-space:nowrap}
  .front-title{top:20px;font-family:'Dosis',sans-serif;font-weight:600;font-size:27px;line-height:32px;letter-spacing:0;text-shadow:0 1px 3px rgba(0,0,0,.25)}
  .front-tagline{top:56px;font-family:'Dancing Script',cursive;font-size:18px;line-height:22px}
  .front-story{top:104px;font-family:'Open Sans',sans-serif;font-style:italic;font-size:12.4px;line-height:13.8px;text-shadow:0 1px 2px rgba(0,0,0,.3)}
  .front-story p{margin-bottom:8px}
  .front-story p + p{border-top:1px solid rgba(255,255,255,.35);padding-top:7px;width:340px;margin-left:53px}
  .front-notes{left:256px;width:446px;top:248px;font-family:'Arimo',sans-serif;font-weight:700;font-size:10.8px;line-height:12.5px;color:var(--white);text-align:center;white-space:nowrap;text-shadow:0 1px 2px rgba(0,0,0,.45)}
  .front-notes p:first-child{margin-bottom:8px}
  .contact-band{background:var(--orange);color:var(--white);font-family:'Open Sans',sans-serif}
  .contact-band--front{left:0;top:302px;width:100%;height:52px;text-align:center;font-size:11.2px;line-height:15px;padding-top:3px}
  .contact-band strong{font-weight:600}

  /* back */
  .back-photo{left:0;top:0;width:100%;height:100%;background:linear-gradient(180deg,var(--back-blue) 0%,var(--back-blue) 45%,var(--back-blue-low) 100%)}
  .back-title{top:20px;font-family:'Dosis',sans-serif;font-weight:600;font-size:28px;line-height:32px;color:var(--white);display:flex;justify-content:center;align-items:center;gap:12px}
  .back-title svg{width:24px;height:32px}
  .back-title::after{content:"";position:absolute;left:190px;right:190px;bottom:-6px;height:1px;background:rgba(255,255,255,.35)}
  .flight-list{left:54px;top:68px;list-style:none;font-family:'Comfortaa',sans-serif;font-size:12.3px;color:var(--white);white-space:nowrap;text-shadow:0 1px 2px rgba(0,0,0,.2)}
  .flight-list li{display:flex;align-items:center;gap:8px;height:20px}
  .flight-list svg{width:16px;height:11px;flex:none}
  .dome{left:-6px;top:156px;width:320px;height:210px}
  .dome-copy{left:0;width:300px;top:220px;font-family:'Open Sans',sans-serif;font-style:italic;font-size:13px;line-height:15.3px;color:var(--white);text-align:center;white-space:nowrap;text-shadow:0 1px 2px rgba(0,0,0,.3)}
  .dome-copy p + p{margin-top:15px}
  .polaroid{background:var(--paper);padding:6px 6px 0;box-shadow:0 3px 8px rgba(0,0,0,.3)}
  .polaroid .shot{height:88px}
  .polaroid figcaption{font-family:'Caveat',cursive;font-size:11px;line-height:10px;color:#333;text-align:center;padding-top:5px}
  .polaroid--one{left:304px;top:150px;width:124px;height:134px;transform:rotate(-5deg)}
  .polaroid--one .shot{background:linear-gradient(180deg,#2c2a3a,#d4532a 55%,#2a2a2a)}
  .polaroid--two{left:431px;top:156px;width:134px;height:134px}
  .polaroid--two .shot{background:linear-gradient(180deg,#3c3f4a,#a7b6c5 40%,#6c7a4a 70%,#5a4a38)}
  .polaroid--three{left:577px;top:152px;width:124px;height:134px;transform:rotate(6deg)}
  .polaroid--three .shot{background:linear-gradient(180deg,#5e8fcf,#a4c0dc 60%,#8a9aa6)}
  .contact-band--back{left:309px;top:306px;width:411px;height:52px;text-align:right;font-size:9.6px;line-height:12px;padding:6px 14px 0 0;white-space:nowrap}
</style>
</head>
<body>
<main class="canvas">

  <section class="card card--front" aria-label="Flyer front">
    <div class="abs hero-photo" role="img" aria-label="Photo of a colourful hot-air balloon rising over misty King Valley hills at dawn, with more balloons in the distance"></div>
    <h1 class="abs front-copy front-title">KING VALLEY HOT-AIR BALLOONING</h1>
    <p class="abs front-copy front-tagline">The perfect gourmet ballooning experience</p>
    <div class="abs front-copy front-story">
      <p>Live the romance and adventure of flying the beautiful<br>King Valley and surrounds in a hot-air balloon at dawn.</p>
      <p>From the vineyards and patchwork of fields the views<br>expand to the Ovens River, spectacular Mt Buffalo and<br>the High Country beyond.</p>
      <p>The mountain views, once aloft, come to life in dramatic<br>3D with the early morning light</p>
    </div>
    <div class="abs front-notes">
      <p>Celebrate your flight with a delicious breakfast afterwards (optional)</p>
      <p>Milawa is conveniently located less than an hour's drive from most places in<br>Victoria's North East and Albury in NSW Mansfield flights are also available</p>
    </div>
    <footer class="abs contact-band contact-band--front">
      For bookings or more information: <strong>www.skylarkaerialtours.com.au</strong><br>
      <strong>flights@skylarkaerialtours.com.au</strong> or call our friendly team on <strong>1300 555 012</strong><br>
      Find us also on our social channels and review sites: <strong>@skylarkaerialtoursaustralia</strong>
    </footer>
  </section>

  <section class="card card--back" aria-label="Flyer back">
    <div class="abs back-photo" role="img" aria-label="Soft photo of a misty blue dawn sky with faint balloons"></div>
    <h2 class="abs center back-title">
      <svg viewBox="0 0 24 32" aria-hidden="true"><path d="M12 1C5.5 1 1 5.6 1 11.5 1 17 6.5 21 9 24h6c2.5-3 8-7 8-12.5C23 5.6 18.5 1 12 1z" fill="var(--orange-light)"/><path d="M12 1c-3 0-4.5 5-4.5 10.5S9.5 21 10.5 24h3c1-3 3-7 3-12.5S15 1 12 1z" fill="var(--orange)"/><rect x="9.5" y="26" width="5" height="5" fill="#8a4a22"/></svg>
      YOUR FLIGHT
      <svg viewBox="0 0 24 32" aria-hidden="true"><path d="M12 1C5.5 1 1 5.6 1 11.5 1 17 6.5 21 9 24h6c2.5-3 8-7 8-12.5C23 5.6 18.5 1 12 1z" fill="var(--orange-light)"/><path d="M12 1c-3 0-4.5 5-4.5 10.5S9.5 21 10.5 24h3c1-3 3-7 3-12.5S15 1 12 1z" fill="var(--orange)"/><rect x="9.5" y="26" width="5" height="5" fill="#8a4a22"/></svg>
    </h2>
    <ul class="abs flight-list">
      <li><svg viewBox="0 0 16 11" aria-hidden="true"><path d="M4 11a3.5 3.5 0 010-7 4.5 4.5 0 018.5-1A3.5 3.5 0 0112.5 11z" fill="var(--white)"/></svg>One-hour sunrise balloon flight in the spectacular King Valley region in North East Victoria</li>
      <li><svg viewBox="0 0 16 11" aria-hidden="true"><path d="M4 11a3.5 3.5 0 010-7 4.5 4.5 0 018.5-1A3.5 3.5 0 0112.5 11z" fill="var(--white)"/></svg>Delicious champagne breakfast after the flight (recommended option)</li>
      <li><svg viewBox="0 0 16 11" aria-hidden="true"><path d="M4 11a3.5 3.5 0 010-7 4.5 4.5 0 018.5-1A3.5 3.5 0 0112.5 11z" fill="var(--white)"/></svg>Informative details throughout your experience with our locally based expert crew</li>
      <li><svg viewBox="0 0 16 11" aria-hidden="true"><path d="M4 11a3.5 3.5 0 010-7 4.5 4.5 0 018.5-1A3.5 3.5 0 0112.5 11z" fill="var(--white)"/></svg>The opportunity to be involved in the inflation and deflation process should you wish</li>
    </ul>

    <svg class="abs dome" viewBox="0 0 320 210" role="img" aria-label="Large orange striped balloon illustration">
      <path d="M0 210V120C0 40 70 0 160 0s160 40 160 120v90z" fill="var(--orange-dome)"/>
    </svg>
    <div class="abs dome-copy">
      <p>Safe, friendly and professional<br>The flight lasts approximately 1 hour<br>The entire experience takes about 3-4 hours<br>Suitable from age 7 to 97<br>Gift Vouchers are also available</p>
      <p>Contact us for exclusive flight options<br>at your custom location</p>
    </div>

    <figure class="abs polaroid polaroid--one">
      <div class="shot" role="img" aria-label="Photo of balloons being inflated with burner flames before dawn"></div>
      <figcaption>Take in the beautiful King Valley and surrounds in your balloon at dawn</figcaption>
    </figure>
    <figure class="abs polaroid polaroid--two">
      <div class="shot" role="img" aria-label="Photo of a balloon basket landing near a winery restaurant"></div>
      <figcaption>Breakfast at Hillcrest Estate Vine Table Restaurant on our return</figcaption>
    </figure>
    <figure class="abs polaroid polaroid--three">
      <div class="shot" role="img" aria-label="Photo of two balloons over misty plains and distant mountains"></div>
      <figcaption>The views expand to the Ovens River, Mt Buffalo and High Country beyond</figcaption>
    </figure>

    <footer class="abs contact-band contact-band--back">
      For bookings or more information: <strong>www.skylarkaerialtours.com.au</strong><br>
      <strong>flights@skylarkaerialtours.com.au</strong> or call our friendly team on <strong>1300 555 012</strong><br>
      Find us also on our social channels and review sites: <strong>@skylarkaerialtoursaustralia</strong>
    </footer>
  </section>

</main>
</body>
</html>
```